2957 Corliss Road Medical Centre

We are looking for a design for new medical clinic.
We are accepting new patients at this new medical centre grand opening. Walk-ins are welcome.
Our cardiac and vascular surgical specialists are department heads at Brenwood Vale Hospital, a leading teaching hospital in Toronto. These specialists will see cardiovascular consults are well as pre-surgical and post-surgical consultations and follow-ups.
Our lab is affiliated with several nuclear medicine clinics in the GTA.
Our Services Includes:
Family Practice
Cardiology Diagnostics
Cardiac & Vascular Surgical Consultation
Ultrasound & Vascular Testing
Open 6 days a week.
Ample Free Parking
Friendly Staffs

Target Market(s)

New Patients. Families of any age. Ethnic groups including Asians & Africans.

Industry/Entity Type

Medical

Font styles to use
Serif
Sans Serif
Decorative
Script
Other font styles liked:
• Arial calibri, verdana

Requirements
Must have
• Address:
• 2957 Corliss Road West
• Unit 418
• Fernhill, Northvale
• K7P 2H9
• Tel: (555) 384-2760
Nice to have
• Caring and inviting environment.
• Simple but classy.
• Standout colors.
Should not have
• Busy images. Aside from this, any ideas are welcome.

```html
<!DOCTYPE html>
<html lang="en">
<head>
<meta charset="utf-8">
<title>2957 Medical Clinic – Now Open</title>
<link rel="stylesheet" href="https://fonts.googleapis.com/css2?family=Montserrat:wght@800&family=Roboto+Slab:wght@400;700&display=swap">
<style>
  :root {
    --red: #c8202a;
    --blue: #2b92d3;
    --teal: #087a8c;
    --ink: #111111;
    --white: #ffffff;
    --map-grey: #b5b5b5;
    --photo-light: #eef3f8;
    --photo-mid: #d9e4ee;
  }
  * { margin: 0; padding: 0; box-sizing: border-box; }
  html, body { width: 777px; height: 1200px; overflow: hidden; background: var(--white); }
  .poster {
    position: relative;
    width: 777px;
    height: 1200px;
    overflow: hidden;
    background: var(--white);
    font-family: "Roboto Slab", Georgia, serif;
  }
  .hero { position: absolute; left: 0; top: 0; width: 777px; height: 560px; }
  .ribbon {
    position: absolute;
    left: -60px;
    top: 52px;
    width: 420px;
    height: 48px;
    background: var(--red);
    color: var(--white);
    transform: rotate(-32deg);
    font-family: "Montserrat", Arial, sans-serif;
    font-weight: 800;
    font-size: 34px;
    line-height: 48px;
    text-align: center;
    letter-spacing: 1px;
  }
  .brand-mark {
    position: absolute;
    left: 136px;
    top: 112px;
    width: 128px;
    height: 128px;
    background: var(--red);
  }
  .brand-name {
    position: absolute;
    left: 300px;
    top: 78px;
    width: 450px;
    text-align: center;
    color: var(--red);
    font-family: "Montserrat", Arial, sans-serif;
    font-weight: 800;
    letter-spacing: -2px;
    line-height: 0.9;
  }
  .brand-name .num { display: block; font-size: 62px; }
  .brand-name .word1 { display: block; font-size: 76px; }
  .brand-name .word2 { display: block; font-size: 76px; }
  .info {
    position: absolute;
    left: 0;
    top: 548px;
    width: 777px;
    text-align: center;
  }
  .headline { color: var(--red); font-weight: 700; font-size: 38px; line-height: 44px; }
  .subline { color: var(--red); font-weight: 700; font-size: 27px; line-height: 31px; }
  .services-title { color: var(--ink); font-weight: 700; font-size: 27px; line-height: 32px; margin-top: 8px; }
  .services { list-style: none; color: var(--ink); font-size: 23px; line-height: 30px; }
  .services li { display: inline-block; margin: 0 12px; }
  .services li::before { content: "• "; font-size: 18px; }
  .book { color: var(--red); font-weight: 700; font-size: 22px; line-height: 26px; margin-top: 12px; }
  .phone { color: var(--ink); font-weight: 700; font-size: 37px; line-height: 42px; }
  .location-map {
    position: absolute;
    left: 240px;
    top: 836px;
    width: 275px;
    height: 224px;
    background: var(--map-grey);
  }
  .footer-wave { position: absolute; left: 0; top: 1055px; width: 777px; height: 145px; }
  .address {
    position: absolute;
    left: 0;
    top: 1134px;
    width: 777px;
    text-align: center;
    color: var(--white);
    font-style: normal;
    font-weight: 700;
    font-size: 22px;
    line-height: 28px;
    letter-spacing: -0.5px;
  }
</style>
</head>
<body>
<main class="poster">
  <svg class="hero" viewBox="0 0 777 560" xmlns="http://www.w3.org/2000/svg">
    <defs>
      <linearGradient id="heroTone" x1="0" y1="0" x2="1" y2="1">
        <stop offset="0" stop-color="#eef3f8"/>
        <stop offset="1" stop-color="#d9e4ee"/>
      </linearGradient>
    </defs>
    <path role="img" aria-label="Doctor in a white coat with stethoscope writing with a pen" d="M0 0H777V185C650 360 420 480 0 500Z" fill="url(#heroTone)"/>
    <path d="M0 500C420 480 650 360 777 185V215C650 400 420 515 0 545Z" fill="#087a8c"/>
    <path d="M0 500C420 480 650 360 777 185V195C650 380 420 500 0 525Z" fill="#2b92d3"/>
  </svg>

  <div class="ribbon">NOW OPEN</div>

  <div class="brand-mark" aria-hidden="true"></div>
  <h1 class="brand-name">
    <span class="num">2957</span>
    <span class="word1">MEDICAL</span>
    <span class="word2">CLINIC</span>
  </h1>

  <section class="info">
    <p class="headline">OPEN 6 DAYS A WEEK</p>
    <p class="subline">ACCEPTING NEW PATIENTS</p>
    <p class="subline">WALK-IN PATIENTS WELCOME</p>
    <h2 class="services-title">SERVICES INCLUDES</h2>
    <ul class="services">
      <li>Family Practice</li>
      <li>Cardiology Diagnostics</li><br>
      <li>Cardiac &amp; Vascular Consultations</li>
      <li>Ultrasound &amp; Vascular</li>
    </ul>
    <p class="book">TO BOOK APPOINTMENT, PLEASE CALL</p>
    <p class="phone">(555) 384-2760</p>
  </section>

  <div class="location-map" role="img" aria-label="Street map showing the clinic location on Corliss Road West near the highway"></div>

  <svg class="footer-wave" viewBox="0 0 777 145" xmlns="http://www.w3.org/2000/svg" preserveAspectRatio="none">
    <path d="M0 10C250 -5 520 15 777 30V145H0Z" fill="#087a8c"/>
    <path d="M0 35C260 20 520 40 777 55V145H0Z" fill="#2b92d3"/>
  </svg>

  <address class="address">
    2957 CORLISS ROAD WEST UNIT 418<br>
    FERNHILL, NORTHVALE,&nbsp; K7P 2H9
  </address>
</main>
</body>
</html>
```